Stationery for a private security company, "Tavrel Security Services Ltd."

Needed is a stationery design for a private security company. The designs must show professionalism and that our company mean nothing but business. Watermark of the company logo on the letterhead page is also a must. The final design must represent innovation and professionalism. It would be great if designers could integrate the colours black and silver onto the cards and letterheads..

Thank you

```html
<!DOCTYPE html>
<html lang="en">
<head>
<meta charset="utf-8">
<title>Tavrel Security Services Ltd. — Stationery</title>
<link rel="stylesheet" href="https://fonts.googleapis.com/css2?family=Cinzel:wght@700&family=Arimo:wght@400;700&family=Dancing+Script:wght@600&display=swap">
<style>
  :root {
    --desk: #ededed;
    --paper: #ffffff;
    --ink: #1a1a1a;
    --ink-soft: #555555;
    --silver-light: #f2f2f2;
    --silver-mid: #c9c9c9;
    --silver-dark: #9a9a9a;
    --band-dark: #6d6d6d;
    --mark: #2a2a2a;
    --signature-blue: #2b4f9e;
  }
  * { margin: 0; padding: 0; box-sizing: border-box; }
  html, body { width: 1200px; height: 795px; overflow: hidden; background: var(--desk); }
  body { position: relative; font-family: "Arimo", Arial, sans-serif; color: var(--ink); }

  /* Brand lockup: plain circle mark + name */
  .brand { display: flex; align-items: center; }
  .brand-stacked { flex-direction: column; }
  .brand-mark { flex: none; border-radius: 50%; background: var(--mark); }
  .brand-name {
    font-family: "Cinzel", Georgia, serif;
    font-weight: 700;
    color: var(--ink);
    line-height: 1;
    text-align: center;
    letter-spacing: 0.02em;
  }
  .brand-name .line { display: block; color: var(--ink); }
  .brand-inline .brand-name { text-align: left; }

  /* Letterhead */
  .letterhead {
    position: absolute; left: 293px; top: 127px; width: 285px; height: 388px;
    background: var(--paper); overflow: hidden;
  }
  .letterhead-header {
    height: 50px;
    background: linear-gradient(180deg, var(--silver-light), var(--silver-mid) 70%, var(--silver-light));
    display: flex; align-items: center; justify-content: center;
  }
  .letterhead-header .brand { gap: 3px; }
  .letterhead-header .brand-mark { width: 16px; height: 16px; }
  .letterhead-header .brand-name { font-size: 11px; }
  .letterhead-header .brand-name .line + .line { font-size: 5.5px; margin-top: 2px; }
  .letterhead-band { height: 7px; background: linear-gradient(90deg, var(--silver-mid), var(--band-dark) 50%, var(--silver-mid)); }
  .letter-watermark {
    position: absolute; left: 10px; top: 200px; width: 275px; height: 190px;
    background: radial-gradient(ellipse 60% 55% at 62% 55%, #d2d2d2, #e6e6e6 55%, rgba(255,255,255,0) 100%);
  }
  .letter-body {
    position: relative; padding: 8px 40px 0 44px; font-size: 4.1px; line-height: 1.6; color: var(--ink-soft);
  }
  .letter-body .date { font-weight: 700; color: var(--ink); margin-bottom: 8px; }
  .letter-body p { margin-bottom: 6px; text-align: justify; }
  .letter-body .signature { font-family: "Dancing Script", cursive; font-size: 10px; line-height: 1.2; color: var(--signature-blue); }
  .letter-body .sender { font-weight: 700; color: var(--ink); }
  .contact-line { font-size: 3.2px; color: var(--ink-soft); text-align: center; line-height: 1.6; }
  .letterhead .contact-line { position: absolute; left: 0; right: 0; bottom: 8px; }

  /* Pencil */
  .pencil {
    position: absolute; left: 232px; top: 300px; width: 8px; height: 210px;
    background: linear-gradient(90deg, var(--band-dark), var(--silver-dark) 50%, var(--band-dark));
  }
  .pencil-tip { position: absolute; left: 232px; top: 272px; width: 8px; height: 28px; }
  .pencil-label {
    position: absolute; left: 50%; top: 165px; transform: translateX(-50%) rotate(90deg);
    font-size: 6px; font-weight: 700; color: var(--paper); letter-spacing: 0.1em; white-space: nowrap;
  }

  /* Folder */
  .folder {
    position: absolute; left: 632px; top: 77px; width: 275px; height: 440px;
    background: linear-gradient(160deg, var(--silver-light), var(--silver-mid) 55%, var(--silver-dark));
    overflow: hidden;
  }
  .folder .brand { position: absolute; top: 46px; left: 0; right: 0; gap: 6px; }
  .folder .brand-mark { width: 38px; height: 38px; }
  .folder .brand-name { font-size: 19px; }
  .folder .brand-name .line + .line { font-size: 8.5px; margin-top: 3px; }
  .folder-artwork {
    position: absolute; left: 0; top: 145px; width: 275px; height: 295px;
    background: linear-gradient(125deg, #d4d4d4 0%, #a8a8a8 22%, #3a3a3a 48%, #1c1c1c 60%, #6a6a6a 78%, #cfcfcf 100%);
    clip-path: polygon(0 0, 100% 8%, 100% 100%, 0 100%);
  }
  .folder-web { position: absolute; bottom: 13px; right: 30px; font-size: 6px; font-weight: 700; color: var(--ink); }

  /* Business cards */
  .card { position: absolute; left: 195px; width: 105px; height: 70px; overflow: hidden; }
  .card-front { top: 548px; background: var(--paper); }
  .card-back {
    top: 630px;
    background: linear-gradient(180deg, var(--silver-mid), var(--silver-light) 55%, var(--paper));
  }
  .card-front .holder { position: absolute; left: 46px; top: 5px; font-size: 3.8px; font-weight: 700; }
  .card-front .holder span { display: block; font-weight: 400; color: var(--ink-soft); font-size: 3px; }
  .card-front .brand { position: absolute; left: 5px; top: 22px; gap: 3px; }
  .card-front .brand-mark { width: 14px; height: 14px; }
  .card-front .brand-name { font-size: 9px; }
  .card-front .brand-name .line + .line { font-size: 4.2px; margin-top: 2px; }
  .card-front .contact-line { position: absolute; left: 44px; top: 45px; text-align: left; }
  .card-back .brand { position: absolute; left: 0; right: 0; top: 14px; justify-content: center; gap: 4px; }
  .card-back .brand-mark { width: 26px; height: 26px; }
  .card-back .brand-name { font-size: 9px; }
  .card-back .web { position: absolute; left: 8px; bottom: 5px; font-size: 3px; color: var(--ink-soft); }

  /* Envelopes */
  .envelope { position: absolute; top: 548px; height: 152px; background: var(--paper); overflow: hidden; }
  .envelope-front { left: 351px; width: 280px; }
  .envelope-front .brand { position: absolute; left: 12px; top: 18px; gap: 4px; }
  .envelope-front .brand-mark { width: 18px; height: 18px; }
  .envelope-front .brand-name { font-size: 11px; }
  .envelope-front .brand-name .line + .line { font-size: 5px; margin-top: 2px; }
  .envelope-back { left: 656px; width: 347px; }
  .envelope-flap { position: absolute; left: 0; top: 0; }
  .envelope-back .brand { position: absolute; left: 0; right: 0; top: 20px; justify-content: center; gap: 4px; }
  .envelope-back .brand-mark { width: 18px; height: 18px; }
  .envelope-back .brand-name { font-size: 9px; }
  .envelope-back .brand-name .line + .line { font-size: 4.5px; margin-top: 2px; }
  .envelope-back .contact-line { position: absolute; left: 0; right: 0; bottom: 7px; }
</style>
</head>
<body>

  <section class="letterhead" aria-label="Letterhead">
    <header class="letterhead-header">
      <div class="brand brand-stacked">
        <span class="brand-mark"></span>
        <div class="brand-name"><span class="line">TAVREL</span><span class="line">Security Services Ltd.</span></div>
      </div>
    </header>
    <div class="letterhead-band"></div>
    <div class="letter-watermark" role="img" aria-label="Faint company emblem watermark"></div>
    <div class="letter-body">
      <div class="date">Date: June, 23 2014</div>
      <p>Dear Customer,</p>
      <p>Thank you for choosing our team to protect your premises. Our trained officers provide round-the-clock patrols, access control, alarm response and visitor screening tailored to your site, your staff and your working hours. Each officer is vetted, licensed and briefed on your building before the first shift begins, and a supervisor visits regularly to check standards, review logs and answer any questions your managers may raise. We believe good security is quiet, visible and dependable, and that it should support the daily work of your business rather than slow it down in any way.</p>
      <p>Every assignment begins with a careful survey of the site. We walk the grounds with your team, note entrances, blind spots, lighting and parking, and look at how people and deliveries move through the day. From this survey we prepare a written security plan that sets out posts, patrol routes, reporting lines and emergency steps. The plan is agreed with you before duty starts and is reviewed every quarter, or sooner whenever your operations, opening hours or building layout change.</p>
      <p>Our control room monitors every post through the night and keeps clear records of each incident, visitor, key issue and patrol. Reports are sent to you each morning, and urgent matters are passed to your named contact at once by phone. Cameras, alarms and radios are tested on every shift, and any fault is logged and fixed quickly so that cover is never interrupted, even during holidays or busy seasonal periods.</p>
      <p>We would be glad to meet with you to discuss this proposal in more detail. Our account manager can arrange a visit at a time that suits you, answer questions about staffing, training and costs, and prepare a final agreement for signature. Once the agreement is in place, our officers can be on site within a few days. Please contact our office with any questions. We look forward to working with you and keeping your people, your property and your business safe every day of the year.</p>
      <p>Regards,</p>
      <div class="signature">Signature</div>
      <div class="sender">SENDER NAME</div>
      <div>Designation</div>
    </div>
    <div class="contact-line">22 Harbour Road, Suite 4, Port City &nbsp; +012 345 6789<br>info@tavrelsecurity.com &nbsp; www.TavrelSecurityServices.com</div>
  </section>

  <svg class="pencil-tip" viewBox="0 0 8 28" aria-hidden="true">
    <polygon points="0,28 8,28 4,0" fill="#e2d3b8"/>
    <polygon points="2.8,6 5.2,6 4,0" fill="#333"/>
  </svg>
  <div class="pencil"><span class="pencil-label">TAVREL</span></div>

  <section class="folder" aria-label="Presentation folder">
    <div class="brand brand-stacked">
      <span class="brand-mark"></span>
      <div class="brand-name"><span class="line">TAVREL</span><span class="line">Security Services Ltd.</span></div>
    </div>
    <div class="folder-artwork" role="img" aria-label="Large company emblem artwork in black and silver"></div>
    <div class="folder-web">www.TavrelSecurityServices.com</div>
  </section>

  <section class="card card-front" aria-label="Business card front">
    <div class="holder">CARDHOLDER NAME<span>Designation</span></div>
    <div class="brand brand-inline">
      <span class="brand-mark"></span>
      <div class="brand-name"><span class="line">TAVREL</span><span class="line">Security Services Ltd.</span></div>
    </div>
    <div class="contact-line">22 Harbour Road, Suite 4, Port City<br>+012 345 6789<br>info@tavrelsecurity.com</div>
  </section>

  <section class="card card-back" aria-label="Business card back">
    <div class="brand brand-inline">
      <span class="brand-mark"></span>
      <div class="brand-name"><span class="line">TAVREL</span></div>
    </div>
    <div class="web">www.TavrelSecurityServices.com</div>
  </section>

  <section class="envelope envelope-front" aria-label="Envelope front">
    <div class="brand brand-inline">
      <span class="brand-mark"></span>
      <div class="brand-name"><span class="line">TAVREL</span><span class="line">Security Services Ltd.</span></div>
    </div>
  </section>

  <section class="envelope envelope-back" aria-label="Envelope back">
    <svg class="envelope-flap" width="347" height="70" viewBox="0 0 347 70" aria-hidden="true">
      <defs>
        <linearGradient id="flap-silver" x1="0" y1="0" x2="0" y2="1">
          <stop offset="0" stop-color="#bdbdbd"/>
          <stop offset="1" stop-color="#ececec"/>
        </linearGradient>
      </defs>
      <path d="M0 0 H347 V38 Q300 66 173 66 Q47 66 0 38 Z" fill="url(#flap-silver)"/>
    </svg>
    <div class="brand brand-inline">
      <span class="brand-mark"></span>
      <div class="brand-name"><span class="line">TAVREL</span><span class="line">Security Services Ltd.</span></div>
    </div>
    <div class="contact-line">22 Harbour Road, Suite 4, Port City &nbsp; +012 345 6789 &nbsp; info@tavrelsecurity.com &nbsp; www.TavrelSecurityServices.com</div>
  </section>

</body>
</html>
```